Sleek, Professional Business Card Design Needed

Business Cards - Logo Attached.

We are a solar consulting company. We are national and want our cards to represent the professional high quality products that we offer.

Industry/Entity Type

Business

Contact Information for Business Card

n/a

Requirements
Must have
• Design
• Name
• Position
• Number
• Email
• Address
Should not have
• Not be too crowded

```html
<!DOCTYPE html>
<html lang="en">
<head>
<meta charset="utf-8">
<title>Sunvale Consulting – Business Card</title>
<link href="https://fonts.googleapis.com/css2?family=Lato:wght@400;700&display=swap" rel="stylesheet">
<style>
  :root {
    --stage: #e8e5e1;
    --card: #ffffff;
    --ink: #3a3a3a;
    --muted: #5f5f5f;
    --green: #8cc63f;
    --blue: #1b8fd0;
    --ghost: #e3ebf6;
  }
  * { margin: 0; padding: 0; box-sizing: border-box; }
  html, body {
    width: 1200px; height: 1040px; overflow: hidden;
    background: var(--stage);
    font-family: "Lato", Arial, sans-serif;
  }
  .card {
    position: absolute; left: 100px; top: 228px;
    width: 1000px; height: 584px;
    background: var(--card);
    overflow: hidden;
    box-shadow: 0 6px 18px rgba(0,0,0,0.18);
  }
  .card__ghost-ring {
    position: absolute; left: -40px; top: 296px;
    width: 370px; height: 370px;
  }
  .person { position: absolute; left: 56px; top: 44px; }
  .person__name {
    font-size: 43px; font-weight: 700; color: var(--ink); line-height: 1.1;
  }
  .person__title {
    font-size: 25px; font-weight: 700; color: var(--green); line-height: 1.2;
  }
  .contact { position: absolute; left: 50px; top: 137px; list-style: none; }
  .contact__item {
    display: flex; align-items: center; height: 34px;
    font-size: 27px; color: var(--muted);
  }
  .contact__icon { width: 22px; height: 22px; margin-right: 26px; flex: none; }
  .brand {
    position: absolute; left: 781px; top: 214px;
    transform: translateX(-50%);
    display: flex; flex-direction: column; align-items: center;
  }
  .brand__mark { width: 150px; height: 150px; }
  .brand__name {
    margin-top: 22px;
    font-size: 36px; font-weight: 700; color: var(--blue);
    white-space: nowrap; letter-spacing: 0.5px;
  }
  .address {
    position: absolute; right: 52px; top: 478px;
    text-align: right; font-size: 27px; line-height: 34px; color: var(--muted);
  }
</style>
</head>
<body>
  <section class="card">
    <svg class="card__ghost-ring" viewBox="0 0 370 370" aria-hidden="true">
      <circle cx="185" cy="185" r="170" fill="none" stroke="var(--ghost)" stroke-width="19"/>
    </svg>

    <header class="person">
      <h1 class="person__name">Dana Whitfield</h1>
      <p class="person__title">Vice President</p>
    </header>

    <ul class="contact">
      <li class="contact__item">
        <svg class="contact__icon" viewBox="0 0 24 24" aria-hidden="true">
          <path fill="var(--green)" d="M6.6 10.8a15 15 0 0 0 6.6 6.6l2.2-2.2c.3-.3.7-.4 1-.2 1.1.4 2.3.6 3.6.6.6 0 1 .4 1 1V20c0 .6-.4 1-1 1C10.6 21 3 13.4 3 4c0-.6.4-1 1-1h3.5c.6 0 1 .4 1 1 0 1.3.2 2.5.6 3.6.1.3 0 .7-.2 1z"/>
        </svg>
        001 555 0188
      </li>
      <li class="contact__item">
        <svg class="contact__icon" viewBox="0 0 24 24" aria-hidden="true">
          <rect x="2" y="5" width="20" height="14" fill="var(--green)"/>
          <path d="M2 5l10 8 10-8" fill="none" stroke="#fff" stroke-width="1.6"/>
        </svg>
        hello@sunvaleconsult.com
      </li>
      <li class="contact__item">
        <svg class="contact__icon" viewBox="0 0 24 24" aria-hidden="true">
          <g fill="none" stroke="var(--green)" stroke-width="1.8">
            <circle cx="12" cy="12" r="9.5"/>
            <ellipse cx="12" cy="12" rx="4" ry="9.5"/>
            <path d="M2.5 12h19M4 7h16M4 17h16"/>
          </g>
        </svg>
        www.sunvaleconsult.com
      </li>
    </ul>

    <div class="brand">
      <svg class="brand__mark" viewBox="0 0 150 150" aria-hidden="true">
        <circle cx="75" cy="75" r="66" fill="none" stroke="var(--blue)" stroke-width="13"/>
      </svg>
      <p class="brand__name">Sunvale Consulting</p>
    </div>

    <address class="address" style="font-style:normal">
      18250 Harbor Road, Suite 4<br>
      Lakeside, Country 90411
    </address>
  </section>
</body>
</html>
```